Word document template for sales proposals

I am after a template that is simple but impactful. Use of colour to be limited but some for impact would be good. The proposals are for use in the professional technical field.

```html
<!DOCTYPE html>
<html lang="en">
<head>
<meta charset="utf-8">
<title>Our Approach – Proposal Template</title>
<link href="https://fonts.googleapis.com/css2?family=Carlito:wght@400;700&display=swap" rel="stylesheet">
<style>
  :root {
    --brand-blue: #29a9e0;
    --brand-orange: #f7931e;
    --ink: #141414;
    --paper: #ffffff;
  }
  * { margin: 0; padding: 0; box-sizing: border-box; }
  html, body { width: 849px; height: 1200px; overflow: hidden; background: var(--paper); }
  body { font-family: "Carlito", "Calibri", sans-serif; color: var(--ink); }
  .page { position: relative; width: 849px; height: 1200px; }
  .header-band {
    position: absolute; left: 0; top: 110px; width: 617px; height: 23px;
    background: var(--brand-blue);
  }
  .brand {
    position: absolute; left: 627px; top: 99px; display: flex; align-items: center; gap: 8px;
  }
  .brand-dot { width: 38px; height: 38px; border-radius: 50%; background: var(--brand-blue); }
  .brand-name {
    font-size: 36px; font-weight: 700; color: var(--brand-orange); line-height: 1;
  }
  .page-title {
    position: absolute; left: 100px; top: 225px; font-size: 37px; font-weight: 400; line-height: 1.1;
  }
  .section { position: absolute; left: 100px; width: 660px; }
  .section h2 { font-size: 20.5px; font-weight: 400; line-height: 24px; letter-spacing: 0.1px; }
  .section p { font-size: 15.5px; line-height: 22px; letter-spacing: 0.5px; }
  .line-justified {
    display: block; width: var(--w); text-align: justify; text-align-last: justify;
  }
  .steps { list-style: none; margin-top: 12px; }
  .steps li {
    position: relative; padding-left: 50px; font-size: 15.5px; line-height: 22.9px; letter-spacing: 0.5px;
  }
  .steps li::before {
    content: ""; position: absolute; left: 26px; top: 9px; width: 5px; height: 5px;
    border-radius: 50%; background: var(--ink);
  }
</style>
</head>
<body>
<div class="page">
  <div class="header-band"></div>
  <div class="brand">
    <span class="brand-dot"></span>
    <span class="brand-name">Quarnel</span>
  </div>

  <h1 class="page-title">Our Approach</h1>

  <section class="section" style="top:289px">
    <h2>Our Company</h2>
    <p><span class="line-justified" style="--w:618px">Provide a concise summary of your organization, including competitive advantages or</span>differentiation from key competitors.</p>
  </section>

  <section class="section" style="top:377px">
    <h2>Our Solution</h2>
    <p><span class="line-justified" style="--w:633px">Outline an integrated solution that aligns to the prospect’s decision criteria and includes key</span><span class="line-justified" style="--w:626px">deliverables, professional services, service level agreement, and project delivery timelines.</span></p>
  </section>

  <section class="section" style="top:465px">
    <h2>Key Product/Service Offering</h2>
    <p><span class="line-justified" style="--w:620px">List the key components of your product/service and relate the features to the prospect’s</span>need to demonstrate value.</p>
  </section>

  <section class="section" style="top:553px">
    <h2>Professional Services</h2>
    <p>Communicate how you will help with implementation.</p>
  </section>

  <section class="section" style="top:619px">
    <h2>Service Level Agreement</h2>
    <p>Insert your standard service level agreement.</p>
  </section>

  <section class="section" style="top:685px">
    <h2>Project Delivery Timelines</h2>
    <p><span class="line-justified" style="--w:635px">Provide a Project Schedule that includes timelines, deliverables, milestones, and checkpoints.</span></p>
  </section>

  <section class="section" style="top:751px">
    <h2>Action Plan</h2>
    <p><span class="line-justified" style="--w:645px">Create a step-by-step Action Plan that illustrates how your solution will be implemented.</span>Align to the prospect’s purchasing process.</p>
    <ul class="steps">
      <li>Step 1 – provide clarity on this step in the process.</li>
      <li>Step 2 - provide clarity on this step in the process.</li>
      <li>Step 3 – Provide clarity on this step in the process.</li>
      <li>Step 4 - provide clarity on this step in the process.</li>
      <li>Step 5 - provide clarity on this step in the process.</li>
      <li>Step 6 - provide clarity on this step in the process.</li>
      <li>Step 7 - provide clarity on this step in the process.</li>
      <li>Step 8 - provide clarity on this step in the process.</li>
    </ul>
  </section>
</div>
</body>
</html>
```